【タイトル】
超現実派エンジニアも驚く!
メンタル不調も!恋愛の失敗も!実らない努力も!

全ての原因は56種の「モヤリンk」
最強ワークで過去を手放し、人生を全て好転させよう! 

【書籍の特典情報】
誰でもできる
「セルフ解放ワーク」
の動画プレゼント!

【ターゲット】
引き寄せの法則や成功法則が好きな方向け

【著者】
(元システムエンジニア)
企業サポーター
桐野 沙織

【説明】
電子書籍の表紙のデザインをお願いします。

電子書籍なので、タイトル文字を見やすくしてほしいです。

元システムエンジニアで、企業サポーターという職業柄もあり
とても現実派の私が実感して提供しているワークのお話になります

引き寄せやスピリチュアルとは違うので、
どちらかというと成功の法則のように
現実的なイメージの表紙だと良いかなと思っています。

本文をつけますので参考にしていただければと思います。

見た時に、とてもインパクトがあるように感じました。
電子書籍は、表紙の役割が大きいので
わかりやすさもとても大切だと感じ、選ばせていただきました。

皆様、素敵なデザインをご提案いただきありがとうございます。
とても迷い、投票も行い選択させていただきました。
今後、お仕事やデザインをご依頼させていただく際は
また、よろしくお願いいたします。

```html
<!DOCTYPE html>
<html lang="ja">
<head>
<meta charset="UTF-8">
<title>セルフ解放ワーク 表紙</title>
<link rel="stylesheet" href="https://fonts.googleapis.com/css2?family=Noto+Sans+JP:wght@500;700;900&family=Noto+Serif+JP:wght@600;700&display=swap">
<style>
  :root {
    --navy: #1d2f5e;
    --cyan: #2bb3e2;
    --cyan-deep: #1a9fd3;
    --lime: #a9cc2b;
    --white: #ffffff;
  }
  * { margin: 0; padding: 0; box-sizing: border-box; }
  html, body { width: 749px; height: 1200px; overflow: hidden; background: var(--white); }
  .cover {
    position: relative; width: 749px; height: 1200px; overflow: hidden;
    background: var(--white);
    font-family: "Noto Sans JP", sans-serif;
    color: var(--navy);
  }
  .frame { position: absolute; inset: 0; }
  .headline {
    position: absolute; left: 36px; top: 78px;
    font-weight: 900; font-size: 58px; line-height: 1; letter-spacing: 1px;
    white-space: nowrap;
  }
  .headline span {
    display: inline-block; margin-bottom: 11px; padding-bottom: 6px;
    background: linear-gradient(transparent 84%, var(--cyan) 84%, var(--cyan) 94%, transparent 94%);
  }
  .gift-badge {
    position: absolute; left: 512px; top: 162px; width: 218px; height: 138px;
    background: var(--lime); color: var(--white);
    display: flex; flex-direction: column; justify-content: center; align-items: center;
    font-weight: 900; font-size: 27px; line-height: 1.35; text-align: center;
  }
  .anyone {
    position: absolute; left: 632px; top: 372px;
    writing-mode: vertical-rl; font-weight: 700; font-size: 34px; letter-spacing: 6px;
  }
  .bonus-title {
    position: absolute; left: 70px; top: 530px;
    font-weight: 700; font-size: 40px; letter-spacing: 1px; white-space: nowrap;
  }
  .bonus-present {
    position: absolute; left: 222px; top: 590px;
    font-weight: 700; font-size: 48px; color: var(--cyan); letter-spacing: 3px;
  }
  .cause-panel {
    position: absolute; left: 30px; top: 705px; width: 696px; height: 455px;
    background: linear-gradient(180deg, var(--cyan) 0%, var(--cyan-deep) 100%);
    color: var(--white);
  }
  .cause-text {
    position: absolute; left: 44px; top: 10px;
    font-weight: 900; font-size: 52px; line-height: 75px; white-space: nowrap;
  }
  .cause-text .keyword {
    background: linear-gradient(transparent 84%, var(--lime) 84%, var(--lime) 94%, transparent 94%);
  }
  .author {
    position: absolute; left: 422px; top: 168px;
    font-family: "Noto Serif JP", serif; font-weight: 700; line-height: 1.3;
    white-space: nowrap;
  }
  .author .role { font-size: 15px; }
  .author .name { font-size: 32px; letter-spacing: 3px; line-height: 1.4; }
  .author .name small { font-size: 17px; letter-spacing: 0; }
</style>
</head>
<body>
<div class="cover">
  <svg class="frame" width="749" height="1200" viewBox="0 0 749 1200" aria-hidden="true">
    <polyline points="30,100 30,520 612,520" fill="none" stroke="#2bb3e2" stroke-width="3"/>
    <line x1="724" y1="300" x2="724" y2="705" stroke="#2bb3e2" stroke-width="3"/>
  </svg>

  <h1 class="headline">
    <span>超現実派エンジニア</span><br>
    <span>も驚く！</span><br>
    <span>メンタル不調も！</span><br>
    <span>恋愛の失敗も！</span><br>
    <span>実らない努力も！</span>
  </h1>

  <div class="gift-badge">
    <div>読者様</div><div>無料</div><div>プレゼント！</div>
  </div>

  <div class="anyone">誰でもできる</div>
  <div class="bonus-title">「セルフ解放ワーク」動画</div>
  <div class="bonus-present">PRESENT！</div>

  <section class="cause-panel">
    <p class="cause-text">
      全ての原因は<br>
      56種の<span class="keyword">「モヤリンk」</span><br>
      最強ワークで<br>
      過去を手放し、<br>
      人生を全て好転させよう！
    </p>
    <div class="author">
      <div class="role">〈元システムエンジニア〉</div>
      <div class="role">企業サポーター</div>
      <div class="name">桐野 沙織<small>［著］</small></div>
    </div>
  </section>
</div>
</body>
</html>
```